Varlow's Electrical & Solar - Business Cards

I want my business card to stand out from the rest. I will provide my business name logo and my icon logo to be implemented onto the card.

On the front of the card, can i have the following. Just make it neat & professional please.

Dean Harrop
varlowselectrical@mailbox-example.net
0491 837 562
ABN: 41 269 507 813
License No. 582146K
FREE QUOTES
24/7 Emergency

On the back of the card, can I have "Our Services" and maybe add the V logo on the back in the background or something. Under "Our Services" I want the following:

LED Lighting Upgrades
Switches & Outlets
Smoke Alarms
Switchboard Upgrades
Fault Finding
Rewiring
New Builds
Test & Tagging
All Electrical Maintenance & Repairs

Can you guys add the instagram logo and next to it, put varlows_electrical

Can you guys also add the facebook logo and next to it put Varlow's Electrical & Solar. Make sure the instagram & facebook icon is in either white, green or black.

Also I have put down double sided, not sure why when i save it, it keeps going to single sided. I need my business card double sided.

New Customers

Dean Harrop varlowselectrical@mailbox-example.net 0491 837 562 ABN: 41 269 507 813 License No. 582146K FREE QUOTES 24/7 Emergency

• must be tidy, professional and appealing

```html
<!DOCTYPE html>
<html lang="en">
<head>
<meta charset="utf-8">
<title>Varlow's Electrical &amp; Solar – Business Cards</title>
<link rel="stylesheet" href="https://fonts.googleapis.com/css2?family=Questrial&family=Michroma&display=swap">
<style>
  :root {
    --backdrop: #2b2b2d;
    --card: #1c1c1d;
    --card-edge: #262628;
    --green: #2fc93a;
    --silver: #d9dcdf;
    --text: #f1f1f1;
    --rule: #5a5a5c;
  }
  * { box-sizing: border-box; margin: 0; padding: 0; }
  html, body {
    width: 1200px; height: 874px; overflow: hidden;
    background: var(--backdrop);
    font-family: "Questrial", sans-serif;
    color: var(--text);
  }
  .sheet {
    position: relative; width: 1200px; height: 874px;
    display: flex; flex-direction: column; align-items: center; justify-content: center; gap: 34px;
  }
  .card {
    position: relative; width: 640px; height: 380px;
    background: linear-gradient(160deg, var(--card-edge), var(--card));
    border-radius: 22px;
    box-shadow: 0 10px 28px rgba(0,0,0,.45);
    overflow: hidden;
  }

  /* Services side */
  .services { display: flex; flex-direction: column; align-items: center; padding-top: 58px; }
  .brand-name {
    font-size: 38px; font-weight: 400; letter-spacing: 1px; color: var(--green);
    display: flex; align-items: center; gap: 14px; white-space: nowrap;
  }
  .brand-name .mark-dot { width: 22px; height: 22px; border-radius: 50%; background: var(--green); flex: none; }
  .services-heading {
    margin-top: 28px; font-family: "Michroma", sans-serif; font-size: 15px; font-weight: 400;
    letter-spacing: 3px; color: var(--green);
  }
  .service-list { margin-top: 12px; text-align: center; font-size: 18px; line-height: 1.4; white-space: nowrap; }
  .service-list .dot { color: var(--green); padding: 0 7px; }
  .social-row {
    margin-top: 22px; width: 540px; display: flex; align-items: center; gap: 14px; font-size: 17px; white-space: nowrap;
  }
  .social-row .rule { flex: 1; height: 1px; background: var(--rule); }
  .social-item { display: flex; align-items: center; gap: 8px; }
  .social-item .shape-circle { width: 14px; height: 14px; border-radius: 50%; background: var(--green); }
  .social-item .shape-square { width: 13px; height: 13px; border-radius: 3px; background: var(--green); }

  /* Contact side */
  .contact-main { position: absolute; top: 62px; left: 52px; display: flex; align-items: center; }
  .icon-mark {
    width: 150px; height: 150px; border-radius: 50%; border: 7px solid var(--green);
    display: flex; align-items: center; justify-content: center; flex: none;
    font-size: 26px; color: var(--silver);
  }
  .divider { width: 1px; height: 180px; background: var(--rule); margin: 0 26px 0 32px; flex: none; }
  .person-name { font-family: "Michroma", sans-serif; font-weight: 400; font-size: 23px; color: var(--green); margin-bottom: 14px; white-space: nowrap; }
  .contact-line { display: flex; align-items: center; gap: 10px; font-size: 17px; margin-bottom: 7px; white-space: nowrap; }
  .contact-line svg { width: 15px; height: 15px; fill: var(--green); flex: none; }
  .contact-line.email { font-size: 15px; }
  .tagline { position: absolute; bottom: 46px; left: 70px; font-size: 21px; letter-spacing: .5px; white-space: nowrap; }
  .tagline .dot { color: var(--green); padding: 0 10px; }
</style>
</head>
<body>
<main class="sheet">
  <section class="card services" aria-label="Services side">
    <h1 class="brand-name"><span class="mark-dot" aria-hidden="true"></span>Varlow's Electrical &amp; Solar</h1>
    <h2 class="services-heading">OUR SERVICES</h2>
    <div class="service-list">
      <p>LED Lighting Upgrades<span class="dot">•</span>Switches &amp; Outlets<span class="dot">•</span>Smoke Alarms</p>
      <p>Switchboard Upgrades<span class="dot">•</span>Fault Finding<span class="dot">•</span>Rewiring<span class="dot">•</span>New Builds</p>
      <p>Test &amp; Tagging<span class="dot">•</span>All Electrical Maintenance &amp; Repairs</p>
    </div>
    <div class="social-row">
      <span class="rule"></span>
      <span class="social-item"><span class="shape-circle" aria-hidden="true"></span>Varlow's Electrical &amp; Solar</span>
      <span class="social-item"><span class="shape-square" aria-hidden="true"></span>varlows_electrical</span>
      <span class="rule"></span>
    </div>
  </section>

  <section class="card contact" aria-label="Contact side">
    <div class="contact-main">
      <div class="icon-mark">Varlow's</div>
      <span class="divider"></span>
      <div class="details">
        <h2 class="person-name">DEAN HARROP</h2>
        <p class="contact-line">
          <svg viewBox="0 0 24 24" aria-hidden="true"><path d="M6.6 10.8a15.1 15.1 0 0 0 6.6 6.6l2.2-2.2c.3-.3.7-.4 1-.2 1.1.4 2.3.6 3.6.6.6 0 1 .4 1 1V20c0 .6-.4 1-1 1A17 17 0 0 1 3 4c0-.6.4-1 1-1h3.5c.6 0 1 .4 1 1 0 1.3.2 2.5.6 3.6.1.3 0 .7-.2 1z"/></svg>
          0491 837 562
        </p>
        <p class="contact-line email">
          <svg viewBox="0 0 24 24" aria-hidden="true"><path d="M2 5h20v14H2zm2 2v.5l8 5 8-5V7l-8 5z"/></svg>
          varlowselectrical@mailbox-example.net
        </p>
        <p class="contact-line">ABN: 41 269 507 813</p>
        <p class="contact-line">License No. 582146K</p>
      </div>
    </div>
    <p class="tagline">FREE QUOTES<span class="dot">•</span>24/7 Emergency</p>
  </section>
</main>
</body>
</html>
```